TV - business card

Tidewell Vantage is an insurance brokerage firm, inovative, proactive, vigorous, which aims to become the leader of the insurance brokers in Anfrica. We should like to get some designs which should be avoided also in Gray / Metallic for the Administration and Orange / Blue for the Managers (ike in the picture sent). The Blue / Green logo is not the correct one, but the source of the file. Please adjust the color accordingly for the business cards. 1 / Orange / Blue 2 / Gray / Metallic We want something classic but which is transmitted strenght, inovation, modernity and most of all, rapidity. We want something start-up like, very punchy and catching eye remaining profesional at the same time. Name: Delton Ashgrove Function: Managing Director Address: N ° 73/74 Cmt. Bolembe - R / C 2B Esquerda - Bairro Quimbuta - Luanda Tel: (+244) 947 385 619 Email: delton.ashgrove@tidewell-v.com Website: www.tidewell-v. com We want classic in the front and creative, colorfull at the back. The cards will be printed in relief, with very high quality of paper.
Industry/Entity Type
Insurance Broker
Colors
Designer to choose colors to be used in the design.
Look and feel

```html
<!DOCTYPE html>
<html lang="en">
<head>
<meta charset="utf-8">
<title>Tidewell Vantage – Business Card</title>
<link rel="stylesheet" href="https://fonts.googleapis.com/css2?family=Mulish:wght@400;500;700;800&display=swap">
<style>
  :root {
    --page-bg: #1b1b1b;
    --card-bg: #232323;
    --card-edge: #2c2c2c;
    --metal: #b9b9bb;
    --metal-dark: #7d7d80;
    --accent-blue: #2aa8e0;
    --accent-green: #1f9a4a;
    --ink-light: #f2f2f2;
  }
  * { margin: 0; padding: 0; box-sizing: border-box; }
  html, body {
    width: 1200px;
    height: 900px;
    overflow: hidden;
    background: var(--page-bg);
    font-family: "Mulish", sans-serif;
  }
  .canvas {
    position: relative;
    width: 1200px;
    height: 900px;
  }
  .card {
    position: absolute;
    left: 290px;
    width: 620px;
    height: 354px;
    background: var(--card-bg);
    border: 1px solid var(--card-edge);
    box-shadow: 0 18px 40px rgba(0,0,0,0.55);
  }
  .card--front { top: 68px; }
  .card--back { top: 478px; }

  /* Front */
  .front-brand {
    position: absolute;
    inset: 0;
    display: flex;
    flex-direction: column;
    align-items: center;
    justify-content: center;
    gap: 18px;
  }
  .front-brand__dot {
    width: 74px;
    height: 74px;
    border-radius: 50%;
    border: 6px solid var(--metal-dark);
  }
  .front-brand__name {
    font-weight: 800;
    font-size: 34px;
    letter-spacing: 1px;
    color: var(--metal);
    text-transform: uppercase;
  }

  /* Back */
  .back-brand {
    position: absolute;
    left: 40px;
    top: 0;
    width: 200px;
    height: 100%;
    display: flex;
    flex-direction: column;
    align-items: center;
    justify-content: center;
    gap: 16px;
  }
  .back-brand__dot {
    width: 110px;
    height: 110px;
    border-radius: 50%;
    border: 9px solid var(--accent-green);
  }
  .back-brand__name {
    font-weight: 800;
    font-size: 17px;
    color: var(--accent-blue);
    white-space: nowrap;
  }
  .divider {
    position: absolute;
    left: 272px;
    top: 78px;
    width: 2px;
    height: 196px;
    background: var(--accent-blue);
  }
  .contact {
    position: absolute;
    left: 308px;
    top: 82px;
    color: var(--ink-light);
  }
  .contact__name {
    font-weight: 700;
    font-size: 27px;
    color: var(--accent-blue);
    letter-spacing: 0.5px;
    line-height: 1.05;
  }
  .contact__role {
    font-size: 15px;
    font-weight: 500;
    margin-top: 2px;
  }
  .contact__address {
    font-size: 15px;
    line-height: 1.35;
    margin-top: 14px;
  }
  .contact__lines {
    margin-top: 10px;
    font-size: 15px;
    line-height: 1.45;
  }
  .contact__line {
    display: flex;
    align-items: center;
    gap: 8px;
  }
  .contact__icon { width: 13px; height: 13px; flex: none; }
</style>
</head>
<body>
<main class="canvas">
  <section class="card card--front" aria-label="Card front">
    <div class="front-brand">
      <div class="front-brand__dot"></div>
      <div class="front-brand__name">Tidewell Vantage</div>
    </div>
  </section>

  <section class="card card--back" aria-label="Card back">
    <div class="back-brand">
      <div class="back-brand__dot"></div>
      <div class="back-brand__name">Tidewell Vantage</div>
    </div>
    <div class="divider"></div>
    <div class="contact">
      <div class="contact__name">Delton Ashgrove</div>
      <div class="contact__role">Managing Director</div>
      <div class="contact__address">
        N ° 73/74 Cmt. Bolembe<br>
        R / C 2B Esquerda<br>
        Bairro Quimbuta - Luanda
      </div>
      <div class="contact__lines">
        <div class="contact__line">
          <svg class="contact__icon" viewBox="0 0 24 24" aria-hidden="true"><path fill="#2aa8e0" d="M6.6 10.8a15.1 15.1 0 0 0 6.6 6.6l2.2-2.2c.3-.3.7-.4 1-.2 1.1.4 2.3.6 3.6.6.6 0 1 .4 1 1V20c0 .6-.4 1-1 1A17 17 0 0 1 3 4c0-.6.4-1 1-1h3.5c.6 0 1 .4 1 1 0 1.3.2 2.5.6 3.6.1.3 0 .7-.2 1z"/></svg>
          <span>+244 947 385 619</span>
        </div>
        <div class="contact__line">
          <svg class="contact__icon" viewBox="0 0 24 24" aria-hidden="true"><rect x="2" y="5" width="20" height="14" rx="1.5" fill="none" stroke="#2aa8e0" stroke-width="2.2"/><path d="M3 6l9 7 9-7" fill="none" stroke="#2aa8e0" stroke-width="2.2"/></svg>
          <span>delton.ashgrove@tidewell-v.com</span>
        </div>
      </div>
    </div>
  </section>
</main>
</body>
</html>
```